Investor Slide Deck

Simple idea - take a model investor deck and build out a investor deck for R4M. I will complete the data, I need a template to work from within. I will attach a model investor deck and a blank R4M that I need built out to R4M. Use the R4M Pwrpt to build out the investor deck

```html
<!DOCTYPE html>
<html lang="en">
<head>
<meta charset="utf-8">
<title>R4M Investor Deck 2024</title>
<link href="https://fonts.googleapis.com/css2?family=Poppins:wght@400;500;600;700;800&display=swap" rel="stylesheet">
<style>
  :root {
    --canvas: #eceef0;
    --white: #ffffff;
    --ink: #1f2f36;
    --text: #5c666b;
    --teal-dark: #1d3b45;
    --teal: #1a8a8f;
    --blue: #2f6fb5;
    --orange: #f26b21;
    --yellow: #f7b81c;
    --magenta: #a3155b;
    --green: #3aa76d;
  }
  * { box-sizing: border-box; margin: 0; padding: 0; }
  html, body { width: 1200px; height: 2448px; overflow: hidden; }
  body { background: var(--canvas); font-family: "Poppins", sans-serif; position: relative; color: var(--ink); }

  .hero-wrap { position: absolute; left: 50px; top: 160px; width: 1100px; height: 619px; box-shadow: 0 20px 50px rgba(0,0,0,.18); }
  .hero-wrap .slide { position: absolute; left: 0; top: 0; transform: scale(1.9643); transform-origin: 0 0; box-shadow: none; }

  .slide { position: absolute; width: 560px; height: 315px; background: var(--white); overflow: hidden; box-shadow: 0 6px 18px rgba(0,0,0,.12); }
  .pos-1 { left: 20px; top: 1000px; } .pos-2 { left: 620px; top: 1000px; }
  .pos-3 { left: 20px; top: 1415px; } .pos-4 { left: 620px; top: 1415px; }
  .pos-5 { left: 20px; top: 1830px; } .pos-6 { left: 620px; top: 1830px; }

  .slide-footer { position: absolute; left: 0; right: 0; bottom: 0; height: 24px; background: var(--magenta); display: flex; align-items: center; justify-content: space-between; padding: 0 16px; color: var(--white); font-size: 7px; font-weight: 600; letter-spacing: .5px; }
  .slide-footer .mark { display: flex; align-items: center; gap: 5px; }
  .slide-footer .dot { width: 7px; height: 7px; border-radius: 50%; background: var(--yellow); }

  .heading { font-weight: 800; font-size: 22px; line-height: 1; text-transform: uppercase; color: var(--ink); }
  .body-text { font-size: 7.5px; line-height: 1.55; color: var(--text); }

  /* Cover */
  .slide--cover { background: var(--teal-dark); }
  .cover-logo { position: absolute; left: 34px; top: 36px; font-size: 28px; font-weight: 800; color: var(--orange); }
  .cover-title { position: absolute; left: 34px; top: 112px; font-weight: 800; font-size: 46px; line-height: .95; color: var(--yellow); }
  .cover-year { position: absolute; left: 36px; top: 206px; font-size: 26px; font-weight: 700; color: transparent; -webkit-text-stroke: 1px var(--teal); letter-spacing: 2px; }
  .cover-photo-ring { position: absolute; left: 312px; top: 34px; width: 222px; height: 222px; border-radius: 50%; border: 6px solid var(--yellow); padding: 6px; }
  .cover-photo { width: 100%; height: 100%; border-radius: 50%; background: linear-gradient(135deg, #b9c6cc 0%, #6b8a97 45%, #34505c 100%); }

  /* Problems */
  .problems-left { position: absolute; left: 26px; top: 30px; width: 270px; }
  .problems-left .body-text { margin-top: 12px; }
  .sub-item { margin-top: 14px; }
  .sub-item h4 { font-size: 10px; font-weight: 700; color: var(--orange); text-transform: uppercase; margin-bottom: 3px; }
  .problems-panel { position: absolute; left: 318px; top: 26px; width: 216px; height: 238px; background: var(--teal-dark); padding: 24px 20px; color: var(--white); }
  .problems-panel h3 { font-size: 20px; font-weight: 800; line-height: 1; text-align: right; }
  .problems-panel .panel-sub { font-size: 8px; font-weight: 600; color: var(--orange); text-align: right; margin-top: 3px; letter-spacing: 1px; }
  .case-list { list-style: none; margin-top: 22px; }
  .case-list li { font-size: 8px; font-weight: 600; margin-bottom: 8px; display: flex; align-items: center; gap: 6px; }
  .case-list li::before { content: "›"; color: var(--orange); font-size: 12px; font-weight: 700; line-height: 0; }

  /* Solutions */
  .solutions-left { position: absolute; left: 26px; top: 30px; width: 240px; }
  .solutions-left .body-text { margin-top: 12px; }
  .points-box { position: absolute; left: 290px; top: 22px; width: 246px; height: 250px; border: 2px solid var(--orange); padding: 16px 18px; }
  .points-box h3 { font-size: 15px; font-weight: 800; }
  .point { display: flex; gap: 9px; margin-top: 13px; }
  .point-num { flex: none; width: 20px; height: 20px; border-radius: 50%; color: var(--white); font-size: 9px; font-weight: 700; display: flex; align-items: center; justify-content: center; }
  .point h4 { font-size: 8.5px; font-weight: 700; text-transform: uppercase; }
  .point p { font-size: 6.5px; color: var(--text); line-height: 1.4; }

  /* Company */
  .company-logo { position: absolute; left: 40px; top: 118px; font-size: 40px; font-weight: 800; color: var(--orange); }
  .company-right { position: absolute; left: 200px; top: 26px; width: 330px; }
  .intro-item { display: flex; gap: 12px; margin-top: 16px; }
  .intro-icon { flex: none; width: 30px; height: 30px; border-radius: 50%; }
  .intro-item h4 { font-size: 9px; font-weight: 700; color: var(--orange); text-transform: uppercase; margin-bottom: 2px; }

  /* Market */
  .market-left { position: absolute; left: 26px; top: 30px; width: 160px; }
  .market-left .body-text { margin-top: 12px; }
  .market-chart { position: absolute; left: 200px; top: 28px; }

  /* Thank you */
  .thanks { position: absolute; inset: 0; display: flex; flex-direction: column; align-items: center; justify-content: center; font-weight: 800; line-height: .9; }
  .thanks .t1 { font-size: 70px; color: var(--orange); }
  .thanks .t2 { font-size: 70px; color: var(--magenta); }
</style>
</head>
<body>

<div class="hero-wrap">
  <section class="slide slide--cover">
    <div class="cover-logo">R4M</div>
    <h1 class="cover-title">INVESTOR<br>DECK</h1>
    <div class="cover-year">2024</div>
    <div class="cover-photo-ring"><div class="cover-photo" role="img" aria-label="Photo of a business team meeting in an office"></div></div>
    <footer class="slide-footer"><span class="mark"><span class="dot"></span>R4M | INVESTOR DECK</span><span>2024</span></footer>
  </section>
</div>

<section class="slide slide--cover pos-1">
  <div class="cover-logo">R4M</div>
  <h1 class="cover-title">INVESTOR<br>DECK</h1>
  <div class="cover-year">2024</div>
  <div class="cover-photo-ring"><div class="cover-photo" role="img" aria-label="Photo of a business team meeting in an office"></div></div>
  <footer class="slide-footer"><span class="mark"><span class="dot"></span>R4M | INVESTOR DECK</span><span>01</span></footer>
</section>

<section class="slide pos-2">
  <div class="problems-left">
    <h2 class="heading">Problems</h2>
    <p class="body-text">Replace this paragraph with a short summary of the key point for investors.</p>
    <div class="sub-item"><h4>1. Subheading</h4><p class="body-text">Short supporting detail goes here.</p></div>
    <div class="sub-item"><h4>2. Subheading</h4><p class="body-text">Short supporting detail goes here.</p></div>
  </div>
  <div class="problems-panel">
    <h3>TITLE HERE</h3>
    <div class="panel-sub">SUBHEADING</div>
    <ul class="case-list">
      <li>PROBLEMS CASE STUDY 1</li>
      <li>PROBLEMS CASE STUDY 2</li>
      <li>PROBLEMS CASE STUDY 3</li>
      <li>PROBLEMS CASE STUDY 4</li>
      <li>PROBLEMS CASE STUDY 5</li>
    </ul>
  </div>
  <footer class="slide-footer"><span class="mark"><span class="dot"></span>R4M | INVESTOR DECK</span><span>02</span></footer>
</section>

<section class="slide pos-3">
  <div class="solutions-left">
    <h2 class="heading">Solutions</h2>
    <p class="body-text">Replace this paragraph with a short summary of the key point for investors.</p>
    <p class="body-text">Replace this paragraph with a short summary of the key point for investors.</p>
  </div>
  <div class="points-box">
    <h3>TITLTE</h3>
    <div class="point"><span class="point-num" style="background:var(--orange)">1</span><div><h4>Title Point</h4><p>Short supporting detail goes here.</p></div></div>
    <div class="point"><span class="point-num" style="background:var(--teal)">2</span><div><h4>Title Point</h4><p>Short supporting detail goes here.</p></div></div>
    <div class="point"><span class="point-num" style="background:var(--blue)">3</span><div><h4>Title Point</h4><p>Short supporting detail goes here.</p></div></div>
    <div class="point"><span class="point-num" style="background:var(--green)">4</span><div><h4>Title Point</h4><p>Short supporting detail goes here.</p></div></div>
  </div>
  <footer class="slide-footer"><span class="mark"><span class="dot"></span>R4M | INVESTOR DECK</span><span>03</span></footer>
</section>

<section class="slide pos-4">
  <div class="company-logo">R4M</div>
  <div class="company-right">
    <h2 class="heading" style="font-size:19px">Company Introductions</h2>
    <div class="intro-item"><span class="intro-icon" style="background:var(--orange)"></span><div><h4>Our Vision</h4><p class="body-text">Replace this paragraph with a short summary of the key point for investors.</p></div></div>
    <div class="intro-item"><span class="intro-icon" style="background:var(--teal)"></span><div><h4>Our Mission</h4><p class="body-text">Replace this paragraph with a short summary of the key point for investors.</p></div></div>
    <div class="intro-item"><span class="intro-icon" style="background:var(--yellow)"></span><div><h4>Our Values</h4><p class="body-text">Replace this paragraph with a short summary of the key point for investors.</p></div></div>
  </div>
  <footer class="slide-footer"><span class="mark"><span class="dot"></span>R4M | INVESTOR DECK</span><span>04</span></footer>
</section>

<section class="slide pos-5">
  <div class="market-left">
    <h2 class="heading" style="font-size:19px">Market Data</h2>
    <p class="body-text">Replace this paragraph with a short summary of the key point for investors.</p>
  </div>
  <svg class="market-chart" width="330" height="250" viewBox="0 0 330 250" aria-label="Growth bar chart">
    <defs>
      <linearGradient id="bar-a" x1="0" y1="0" x2="0" y2="1"><stop offset="0" stop-color="#f7b81c"/><stop offset="1" stop-color="#f8d56b"/></linearGradient>
      <linearGradient id="bar-b" x1="0" y1="0" x2="0" y2="1"><stop offset="0" stop-color="#f26b21"/><stop offset="1" stop-color="#f7a06b"/></linearGradient>
      <linearGradient id="bar-c" x1="0" y1="0" x2="0" y2="1"><stop offset="0" stop-color="#1a8a8f"/><stop offset="1" stop-color="#6cc0c2"/></linearGradient>
      <linearGradient id="bar-d" x1="0" y1="0" x2="0" y2="1"><stop offset="0" stop-color="#2f6fb5"/><stop offset="1" stop-color="#7ea7d8"/></linearGradient>
    </defs>
    <line x1="20" y1="230" x2="310" y2="230" stroke="#c9cfd2" stroke-width="1"/>
    <rect x="40" y="170" width="44" height="60" rx="4" fill="url(#bar-a)"/>
    <rect x="105" y="140" width="44" height="90" rx="4" fill="url(#bar-b)"/>
    <rect x="170" y="105" width="44" height="125" rx="4" fill="url(#bar-c)"/>
    <rect x="235" y="65" width="44" height="165" rx="4" fill="url(#bar-d)"/>
    <g font-family="Poppins, sans-serif" font-size="10" font-weight="700" text-anchor="middle">
      <text x="62" y="160" fill="#f7b81c">+5%</text>
      <text x="127" y="130" fill="#f26b21">+10%</text>
      <text x="192" y="95" fill="#1a8a8f">+15%</text>
      <text x="257" y="55" fill="#2f6fb5">+20%</text>
    </g>
    <path d="M30 175 Q 140 150 200 80 T 300 20" fill="none" stroke="#1f2f36" stroke-width="2"/>
    <path d="M300 20 l-11 2 l6 8 z" fill="#1f2f36"/>
  </svg>
  <footer class="slide-footer"><span class="mark"><span class="dot"></span>R4M | INVESTOR DECK</span><span>05</span></footer>
</section>

<section class="slide pos-6">
  <div class="thanks"><span class="t1">THANK</span><span class="t2">YOU</span></div>
</section>

</body>
</html>
```